Coastline Hound Fair Website Bright, colorful, hip

Expo website.
Coastline Hound Fair May 11th, 2019 from 11am-6pm
Wrenfield Green, Baltimore MD
220 Exhibitors from NY to D.C.! Talks on BSL and Animal cruelty! Food Trucks! Live Music! On-Site Adoptions with T.O.K.E.s, Renowned Pitbull advocates Glamgals for Mastiffs and Stand By The Paws, Baltimore rescue Harbors of Hope Tunisia! Games! Contest! Kids Corner!

Target Market(s)

Pet Owners

Industry/Entity Type

Event

Number of Pages Required

2 page

Font styles to use
Sans Serif

Colors

Designer to choose colors to be used in the design.

Requirements
Must have
• Branded header. Slider with "features". Blog page. Google Map of Wrenfield Green.
• "Want to be an exhibitor?!? Click here!"
Nice to have
• Bright and Bold. Super modern
Should not have
• White Space. Dont want to look like the other site I've done on this platform.

```html
<!DOCTYPE html>
<html lang="en">
<head>
<meta charset="utf-8">
<title>Coastline Hound Fair</title>
<link rel="stylesheet" href="https://fonts.googleapis.com/css2?family=Arvo:wght@700&family=Lato:wght@400;700;900&display=swap">
<style>
  :root {
    --gold: #e9b600;
    --yellow: #fcc418;
    --red: #d0021b;
    --ink: #111111;
    --panel: #0c0c0c;
    --page: #1f1f1f;
    --footer: #151515;
    --white: #ffffff;
    --grey-text: #444444;
  }
  * { margin: 0; padding: 0; box-sizing: border-box; }
  html, body { width: 1200px; height: 2311px; overflow: hidden; }
  body { position: relative; background: var(--page); font-family: "Lato", Arial, sans-serif; color: var(--white); }
  .slab { font-family: "Arvo", Georgia, serif; font-weight: 700; }

  /* Hero */
  .hero { position: absolute; left: 0; top: 0; width: 1200px; height: 666px; }
  .hero-photo { position: absolute; inset: 0; background: linear-gradient(180deg, #5f86b0 0%, #8aa6c2 22%, #6b7a6e 36%, #4f6a3a 55%, #3f6b2a 78%, #2f5a22 100%); }
  .hero-shade { position: absolute; inset: 0; background: rgba(0,0,0,0.18); }
  .brand { position: absolute; left: 487px; top: 92px; width: 226px; height: 216px; display: flex; align-items: center; justify-content: center; }
  .brand-ring { position: absolute; inset: 0; border: 4px solid var(--white); border-radius: 50%; }
  .brand-name { position: relative; font-size: 31px; color: var(--white); letter-spacing: 0.5px; text-align: center; line-height: 1.1; }
  .event-title { position: absolute; left: 228px; top: 323px; width: 746px; height: 54px; background: var(--gold); color: var(--white); font-size: 52px; line-height: 56px; text-align: center; text-transform: uppercase; letter-spacing: 0.5px; }
  .event-meta { position: absolute; left: 0; width: 1200px; display: flex; justify-content: center; }
  .event-meta span.row { display: inline-flex; align-items: center; gap: 14px; background: rgba(0,0,0,0.55); padding: 4px 16px; font-size: 28px; text-transform: uppercase; }
  .event-meta svg { flex: none; }
  .date-line { top: 388px; }
  .place-line { top: 443px; }
  .place-line span.row { font-size: 25px; }

  /* Features */
  .features { position: absolute; left: 75px; top: 735px; width: 1051px; height: 414px; background: var(--panel); }
  .features-photo { position: absolute; left: 0; top: 0; width: 421px; height: 414px; background: radial-gradient(ellipse at 50% 45%, #b57a3e 0%, #8a5a2a 35%, #4f7a2c 70%, #3c6a20 100%); }
  .features-title { position: absolute; left: 449px; top: 30px; width: 560px; font-size: 25px; line-height: 31px; text-transform: uppercase; letter-spacing: 0.5px; }
  .features-list { position: absolute; left: 449px; top: 104px; width: 560px; list-style: none; font-size: 15px; }
  .features-list li { position: relative; padding-left: 32px; line-height: 21px; margin-bottom: 11px; }
  .features-list svg { position: absolute; left: 0; top: 5px; }

  /* Blog */
  .blog-heading { position: absolute; left: 0; top: 1220px; width: 1200px; text-align: center; font-size: 23px; text-transform: uppercase; letter-spacing: 0.5px; }
  .post { position: absolute; top: 1272px; width: 330px; height: 375px; }
  .post-photo { position: absolute; left: 0; top: 0; width: 330px; height: 219px; border: 3px solid var(--gold); }
  .post-card { position: absolute; left: 12px; top: 158px; width: 302px; height: 217px; background: var(--white); clip-path: polygon(0 6px, 100% 0, 100% 203px, 0 100%); padding: 32px 18px 0 18px; color: var(--ink); }
  .post-title { font-weight: 700; font-size: 17px; line-height: 23px; text-transform: uppercase; }
  .post-excerpt { margin-top: 9px; font-size: 15px; line-height: 23px; color: var(--grey-text); }
  .post-more { display: inline-block; margin-top: 10px; font-size: 15px; font-weight: 700; color: var(--red); text-decoration: none; }
  .post-1 { left: 75px; } .post-2 { left: 436px; } .post-3 { left: 796px; }
  .post-1 .post-photo { background: linear-gradient(160deg, #2a3a5a 0%, #5a4636 45%, #6b5140 70%, #3a3a3a 100%); }
  .post-2 .post-photo { background: linear-gradient(180deg, #1f4a20 0%, #c9a27a 45%, #e6e0d6 65%, #4a7a2a 100%); }
  .post-3 .post-photo { background: linear-gradient(180deg, #5a8a2a 0%, #c07a3a 45%, #d9b48a 65%, #7aa83a 100%); }

  /* Map */
  .venue-map { position: absolute; left: 0; top: 1702px; width: 1200px; height: 359px; background: linear-gradient(90deg, #e8e6e1 0%, #e8e6e1 34%, #c8e2b8 35%, #c4deb2 68%, #e6e4de 69%, #e6e4de 100%); }
  .venue-card { position: absolute; left: 796px; top: 1779px; width: 329px; height: 204px; background: var(--yellow); border: 4px solid var(--white); box-shadow: 0 2px 8px rgba(0,0,0,0.35); text-align: center; padding-top: 22px; }
  .venue-card h2 { font-size: 25px; line-height: 28px; text-transform: uppercase; color: var(--white); letter-spacing: 0.5px; }
  .venue-name { margin-top: 16px; font-weight: 700; font-size: 20px; color: #6a0d0d; text-transform: uppercase; }
  .venue-place { margin-top: 8px; font-weight: 700; font-size: 15px; color: var(--red); }

  /* Footer */
  .site-footer { position: absolute; left: 0; top: 2061px; width: 1200px; height: 250px; background: var(--footer); text-align: center; }
  .footer-brand { position: absolute; left: 557px; top: 34px; width: 86px; height: 86px; display: flex; align-items: center; justify-content: center; }
  .footer-brand .brand-ring { border-width: 2px; }
  .footer-brand .brand-name { font-size: 13px; }
  .copyright { position: absolute; left: 0; top: 157px; width: 1200px; font-size: 13px; color: #dddddd; }
  .social { position: absolute; left: 0; top: 190px; width: 1200px; display: flex; justify-content: center; gap: 18px; }
  .social span { width: 20px; height: 20px; border-radius: 50%; background: #dddddd; }
</style>
</head>
<body>

<header class="hero">
  <div class="hero-photo" role="img" aria-label="Aerial photo of the Baltimore skyline and a green park under a cloudy blue sky"></div>
  <div class="hero-shade"></div>
  <div class="brand">
    <div class="brand-ring"></div>
    <div class="brand-name slab">Stand By<br>The Paws</div>
  </div>
  <h1 class="event-title slab">Coastline Hound Fair</h1>
  <div class="event-meta date-line slab">
    <span class="row">
      <svg width="26" height="26" viewBox="0 0 26 26" fill="none" stroke="#fff" stroke-width="2"><rect x="2" y="4" width="22" height="20"/><line x1="2" y1="10" x2="24" y2="10"/><line x1="7" y1="1" x2="7" y2="6"/><line x1="19" y1="1" x2="19" y2="6"/><rect x="6" y="14" width="3" height="3" fill="#fff"/><rect x="12" y="14" width="3" height="3" fill="#fff"/><rect x="18" y="14" width="3" height="3" fill="#fff"/><rect x="6" y="19" width="3" height="3" fill="#fff"/><rect x="12" y="19" width="3" height="3" fill="#fff"/></svg>
      May 11th, 2019 from
      <svg width="24" height="24" viewBox="0 0 24 24" fill="none" stroke="#fff" stroke-width="2.5"><circle cx="12" cy="12" r="10"/><polyline points="12,6 12,12 16,14"/></svg>
      11am-6pm
    </span>
  </div>
  <div class="event-meta place-line slab">
    <span class="row">
      <svg width="16" height="24" viewBox="0 0 16 24" fill="#fff"><path d="M8 0C3.6 0 0 3.6 0 8c0 6 8 16 8 16s8-10 8-16c0-4.4-3.6-8-8-8zm0 11a3 3 0 1 1 0-6 3 3 0 0 1 0 6z"/></svg>
      Wrenfield Green, Baltimore MD
    </span>
  </div>
</header>

<section class="features">
  <div class="features-photo" role="img" aria-label="Photo of an English bulldog lying on green grass"></div>
  <h2 class="features-title slab">Some of the happenings in the expo are below:</h2>
  <ul class="features-list">
    <li><svg width="14" height="11" viewBox="0 0 14 11"><polyline points="1,5.5 5,9.5 13,1" fill="none" stroke="#e9b600" stroke-width="2.5"/></svg>220 Exhibitors from NY to D.C.!</li>
    <li><svg width="14" height="11" viewBox="0 0 14 11"><polyline points="1,5.5 5,9.5 13,1" fill="none" stroke="#e9b600" stroke-width="2.5"/></svg>Talks on BSL and Animal cruelty!</li>
    <li><svg width="14" height="11" viewBox="0 0 14 11"><polyline points="1,5.5 5,9.5 13,1" fill="none" stroke="#e9b600" stroke-width="2.5"/></svg>Food Trucks!</li>
    <li><svg width="14" height="11" viewBox="0 0 14 11"><polyline points="1,5.5 5,9.5 13,1" fill="none" stroke="#e9b600" stroke-width="2.5"/></svg>Live Music!</li>
    <li><svg width="14" height="11" viewBox="0 0 14 11"><polyline points="1,5.5 5,9.5 13,1" fill="none" stroke="#e9b600" stroke-width="2.5"/></svg>On-Site Adoptions with T.O.K.E.s, Renowned Pitbull advocates Glamgals for Mastiffs and Stand By The Paws, Baltimore rescue Harbors of Hope Tunisia!</li>
    <li><svg width="14" height="11" viewBox="0 0 14 11"><polyline points="1,5.5 5,9.5 13,1" fill="none" stroke="#e9b600" stroke-width="2.5"/></svg>Games!</li>
    <li><svg width="14" height="11" viewBox="0 0 14 11"><polyline points="1,5.5 5,9.5 13,1" fill="none" stroke="#e9b600" stroke-width="2.5"/></svg>Contest!</li>
    <li><svg width="14" height="11" viewBox="0 0 14 11"><polyline points="1,5.5 5,9.5 13,1" fill="none" stroke="#e9b600" stroke-width="2.5"/></svg>Kids Corner!</li>
  </ul>
</section>

<h2 class="blog-heading slab">Blog Posts</h2>

<article class="post post-1">
  <div class="post-photo" role="img" aria-label="Photo of a brown mastiff at an outdoor dog event"></div>
  <div class="post-card">
    <h3 class="post-title">Nam placerat dui porta ut mi et tincidun</h3>
    <p class="post-excerpt">Sed fermentum diam ac augue ornare semper vitae quis leo. Sed hendrerit sodales ligula in aliquet.</p>
    <a class="post-more" href="#">Read More</a>
  </div>
</article>
<article class="post post-2">
  <div class="post-photo" role="img" aria-label="Photo of a white and brown bulldog standing on grass"></div>
  <div class="post-card">
    <h3 class="post-title">Nam placerat dui porta ut mi et tincidun</h3>
    <p class="post-excerpt">Sed fermentum diam ac augue ornare semper vitae quis leo. Sed hendrerit sodales ligula in aliquet.</p>
    <a class="post-more" href="#">Read More</a>
  </div>
</article>
<article class="post post-3">
  <div class="post-photo" role="img" aria-label="Photo of a bulldog running toward the camera on a lawn"></div>
  <div class="post-card">
    <h3 class="post-title">Nam placerat dui porta ut mi et tincidun</h3>
    <p class="post-excerpt">Sed fermentum diam ac augue ornare semper vitae quis leo. Sed hendrerit sodales ligula in aliquet.</p>
    <a class="post-more" href="#">Read More</a>
  </div>
</article>

<div class="venue-map" role="img" aria-label="Street map of Wrenfield Green and the surrounding Baltimore blocks"></div>
<aside class="venue-card">
  <h2 class="slab">Venue<br>Location</h2>
  <p class="venue-name">Coastline Hound Fair</p>
  <p class="venue-place">Wrenfield Green, Baltimore MD</p>
</aside>

<footer class="site-footer">
  <div class="footer-brand">
    <div class="brand-ring"></div>
    <div class="brand-name slab">Stand By<br>The Paws</div>
  </div>
  <p class="copyright">Copyright © 2018. Company Name. All Right Reserved</p>
  <nav class="social" aria-label="Social links">
    <span></span><span></span><span></span><span></span><span></span>
  </nav>
</footer>

</body>
</html>
```